Professional business cards for real estate development company

I need business cards for my new real estate development company. The company, "KORVA" is a real estate development, investment, and advisory firm with a focus on multifamily, office, and mixed-use projects across primary and secondary markets in the Southeast United States.

Style preference is modern

Industry/Entity Type

Real Estate Development

Contact Information for Business Card

The business cards need to include:
Name
Title
Mailing Address
Phone Number
Web Address

Logo is attached. I would like white to be the primary color with incorporation of the company colors: #232D3A and #B5A451

Font styles to use
Other font styles liked:
• Montserrat, Avenir

Requirements
Must have
• Company Logo. No need to include the company name since the name is in the logo.
Should not have
• No line type designs

```html
<!DOCTYPE html>
<html lang="en">
<head>
<meta charset="utf-8">
<title>KORVA Business Cards</title>
<link rel="stylesheet" href="https://fonts.googleapis.com/css2?family=Montserrat:wght@400;600&display=swap">
<style>
  :root {
    --page: #f2f2f2;
    --card: #fdfdfd;
    --navy: #232d3a;
    --gold: #b5a451;
    --band-grey: #d9dbdb;
    --ink-light: #ffffff;
    --edge: #e2e2e2;
  }
  * { box-sizing: border-box; margin: 0; padding: 0; }
  html, body {
    width: 1005px;
    height: 1200px;
    overflow: hidden;
    background: var(--page);
  }
  .sheet {
    position: relative;
    width: 1005px;
    height: 1200px;
  }
  .card {
    position: absolute;
    left: 102px;
    width: 800px;
    height: 460px;
    background: var(--card);
    border: 1px solid var(--edge);
    border-radius: 22px;
    overflow: hidden;
    box-shadow: 0 8px 24px rgba(0, 0, 0, 0.12);
  }
  .card--front { top: 110px; }
  .card--back { top: 630px; }

  .wordmark {
    font-family: "Montserrat", sans-serif;
    font-weight: 600;
    color: var(--navy);
    letter-spacing: 6px;
    line-height: 1;
  }
  .card--front .wordmark {
    position: absolute;
    left: 0;
    right: 0;
    top: 50%;
    transform: translateY(-50%);
    text-align: center;
    font-size: 72px;
  }

  .band-grey {
    position: absolute;
    left: 0;
    top: 148px;
    width: 470px;
    height: 180px;
    background: var(--band-grey);
    display: flex;
    align-items: center;
    justify-content: center;
  }
  .band-grey .wordmark {
    font-size: 60px;
    padding-left: 40px;
  }
  .band-navy {
    position: absolute;
    left: 465px;
    top: 124px;
    right: 0;
    height: 228px;
    background: var(--navy);
    padding: 22px 0 0 34px;
    font-family: "Montserrat", sans-serif;
  }
  .person-name {
    font-size: 20px;
    font-weight: 600;
    color: var(--gold);
    line-height: 24px;
  }
  .person-title {
    font-size: 13px;
    font-weight: 400;
    color: var(--ink-light);
    letter-spacing: 1px;
    line-height: 18px;
    margin-bottom: 12px;
  }
  .contact-list {
    list-style: none;
    font-size: 16px;
    font-weight: 400;
    color: var(--ink-light);
  }
  .contact-list li {
    display: flex;
    align-items: center;
    gap: 12px;
    height: 30px;
  }
  .contact-list svg {
    width: 17px;
    height: 17px;
    flex: none;
  }
</style>
</head>
<body>
<main class="sheet">
  <section class="card card--front" aria-label="Card front">
    <div class="wordmark">KORVA</div>
  </section>

  <section class="card card--back" aria-label="Card back">
    <div class="band-grey">
      <div class="wordmark">KORVA</div>
    </div>
    <div class="band-navy">
      <p class="person-name">your name here</p>
      <p class="person-title">your title here</p>
      <ul class="contact-list">
        <li>
          <svg viewBox="0 0 24 24" aria-hidden="true"><path fill="#b5a451" d="M3 8c0-3 4-4 9-4s9 1 9 4v2h-4V8.5c-1.5-.6-3.2-.8-5-.8s-3.5.2-5 .8V10H3zM6 11l2-2h8l2 2v8H6zm4 2v1.5h1.5V13zm3 0v1.5h1.5V13zm-3 3v1.5h1.5V16zm3 0v1.5h1.5V16z"/></svg>
          your contact here
        </li>
        <li>
          <svg viewBox="0 0 24 24" aria-hidden="true"><rect x="2.5" y="5" width="19" height="14" rx="1.5" fill="none" stroke="#b5a451" stroke-width="2"/><path d="M3 6l9 7 9-7" fill="none" stroke="#b5a451" stroke-width="2"/></svg>
          your email id here
        </li>
        <li>
          <svg viewBox="0 0 24 24" aria-hidden="true"><path fill="#b5a451" d="M12 2a7 7 0 0 0-7 7c0 5 7 13 7 13s7-8 7-13a7 7 0 0 0-7-7zm0 9.5A2.5 2.5 0 1 1 12 6.5a2.5 2.5 0 0 1 0 5z"/></svg>
          your address here
        </li>
        <li>
          <svg viewBox="0 0 24 24" aria-hidden="true"><g fill="none" stroke="#b5a451" stroke-width="1.6"><circle cx="12" cy="12" r="9.5"/><ellipse cx="12" cy="12" rx="4" ry="9.5"/><path d="M2.5 12h19M4 7h16M4 17h16"/></g></svg>
          your website here
        </li>
      </ul>
    </div>
  </section>
</main>
</body>
</html>
```